PixelGuild CEO Needs a Graphic for a Blog About Crowdsourcing and Online Employment

We need a simple graphic / banner for a blog post that's going to be posted on a large publication (like ByteHerald, Dunmore Commerce Quarterly).

The article will be written by Boris Tandy (PixelGuild's CEO) and the title will be "Why Websites Will Become the Biggest Employers in the World". The article is about why online employers (like PixelGuild and Taskmeadow) will one day have more 'workers' than offline employers.

We'd really like to get this ASAP - so early submissions encouraged. We will try and get the winning designer linked to from the article.

Note that this brief is similar to a previous project that we ran http://jobs.pixelguild.example/job.aspx?id=51734 where the article and design was published on ByteHerald http://byteherald.example/2012/12/08/asias-secret-crowdsourcing-boom/ and the designer (Marabel) was linked to from ByteHerald.

Target Market(s)

Entrepreneurs, journalists, small business owners, tech people.

Industry/Entity Type

Business

Requirements
Must have
• The graphic SHOULD have:
1) Have the text "Why Websites Will Become the Biggest Employers in the World" with some nice design and fonts (consider grey subtle pattern background and white drop shadow on fonts) - see attached examples
2) Have the dimensions 640px wide by 240px wide
Nice to have
• The graphic COULD have:

1) Incorporate the following words in the background (like a word cloud): crowdsource, microtask, crowdfund, witkey, outsource, freelance, online, work from home

OR

2) Incorporate logos of new online employers (Taskmeadow, vRoom, PixelGuild, ChoreOtter, Lanqiufen, GearworkPilot, Framequarry) into the design. If the background of the graphic is grey, ideally, these logos would also be greyscale i.e. they should form a background motif.

OR

3) Show some graphic communicating themes from the article e.g. laptop, globe, workers, connections across the globe

OR

4) Have a second line of text "Why Crowdsourcing Websites Will Overtake Traditional Employers"
Should not have
• Should NOT have:
1) Any photos or clipart

```html
<!DOCTYPE html>
<html lang="en">
<head>
<meta charset="utf-8">
<title>Why Websites Will Become the Biggest Employers in the World</title>
<link rel="stylesheet" href="https://fonts.googleapis.com/css2?family=Bebas+Neue&family=Tinos:wght@400&display=swap">
<style>
  :root {
    --bg-light: #e3e3e3;
    --bg-mid: #d4d4d4;
    --bg-dark: #c6c6c6;
    --ink: #262626;
    --accent: #8a1616;
    --highlight: rgba(255, 255, 255, 0.85);
    --map-dark: #2b2b2b;
    --map-light: #8f8f8f;
  }
  html, body {
    margin: 0;
    padding: 0;
    overflow: hidden;
    background: var(--bg-mid);
  }
  .banner {
    position: relative;
    width: 1200px;
    height: 450px;
    overflow: hidden;
    background:
      radial-gradient(ellipse at 35% 40%, var(--bg-light) 0%, var(--bg-mid) 55%, var(--bg-dark) 100%);
  }
  .headline {
    position: absolute;
    left: 36px;
    top: 52px;
    margin: 0;
    font-family: "Bebas Neue", "Oswald", sans-serif;
    font-weight: 400;
    font-size: 80px;
    line-height: 84px;
    letter-spacing: 1px;
    color: var(--ink);
    text-shadow: 0 2px 0 var(--highlight);
  }
  .headline .line {
    display: block;
  }
  .headline .accent {
    color: var(--accent);
  }
  .subheading {
    position: absolute;
    left: 38px;
    top: 308px;
    margin: 0;
    font-family: "Tinos", "Times New Roman", serif;
    font-weight: 400;
    font-size: 31px;
    line-height: 38px;
    color: var(--ink);
    text-shadow: 0 1px 0 var(--highlight);
  }
  .subheading .line {
    display: block;
  }
  .world-map {
    position: absolute;
    left: 790px;
    top: 50px;
    width: 410px;
    height: 330px;
    border-radius: 40% 30% 45% 35%;
    background:
      radial-gradient(ellipse at 60% 75%, var(--map-dark) 0%, rgba(43,43,43,0.55) 35%, rgba(143,143,143,0.25) 70%, rgba(143,143,143,0) 100%);
  }
</style>
</head>
<body>
  <div class="banner">
    <h1 class="headline">
      <span class="line">Why <span class="accent">Websites</span> Will Become</span>
      <span class="line">The Biggest <span class="accent">Employers</span></span>
      <span class="line">In The <span class="accent">World</span></span>
    </h1>
    <p class="subheading">
      <span class="line">Why Crowdsourcing Websites</span>
      <span class="line">Will Overtake Traditional Employers</span>
    </p>
    <div class="world-map" role="img" aria-label="Striped world map with concentric rings radiating from South America"></div>
  </div>
</body>
</html>
```